Theatre Company needs poster for a Christmas show.

We need a poster for an annual Christmas musical show call "A Plum Hush". The style is Jazzy/Lounge Christmas songs. The poster should be a mid-centry modern, Gilt Row-style design. I have attached the past year's poster for reference. The poster should include "VelNOVA Professional Series presents A Plum Hush" the date "December 18th, 2015" our phone number "512-555-0148 ext 207" and our website "vel-nova.org". The poster should also include the logos of our title sponsors (attached).

Target Market(s)

Lakeway, Texas residents, Adults, 21+

Industry/Entity Type

It Company

Font styles to use
Sans Serif

Requirements
Must have
• VelNOVA logo
• Show title "A Plum Hush"
• Date: December 18th, 2015
• Phone number: 512-555-0148 ext 207
• Web site: vel-nova.org
• Sponsor logos at the bottom (attached)
• Mid-century modern, Gilt Row-style design
• Christmas/Winter colors
Nice to have
• Singer/piano/microphone imagery
• cocktail imagery

```html
<!DOCTYPE html>
<html lang="en">
<head>
<meta charset="utf-8">
<title>A Plum Hush — VelNOVA Professional Series</title>
<link rel="stylesheet" href="https://fonts.googleapis.com/css2?family=Oswald:wght@600;700&family=Lobster&family=Roboto+Condensed:wght@700&display=swap">
<style>
  :root {
    --poster-w: 849px;
    --poster-h: 1200px;
    --lemon: #f6e61e;
    --chartreuse: #d9d83a;
    --olive: #6d7419;
    --moss: #3a3f0c;
    --night: #121405;
    --wine: #9a1a14;
    --gold-top: #ffd43c;
    --gold-bottom: #e56a1a;
    --outline-red: #b0160e;
    --band: #ffffff;
    --ink: #1b1b1b;
    --navy: #1d2f6b;
  }
  html, body {
    margin: 0;
    padding: 0;
    width: var(--poster-w);
    height: var(--poster-h);
    overflow: hidden;
    background: #ffffff;
  }
  .poster {
    position: relative;
    width: var(--poster-w);
    height: var(--poster-h);
    overflow: hidden;
    font-family: "Oswald", sans-serif;
  }
  .hero-photo {
    position: absolute;
    left: 0;
    top: 0;
    width: 100%;
    height: 1098px;
    background:
      linear-gradient(90deg, rgba(18,20,5,0.55) 0%, rgba(18,20,5,0) 30%, rgba(18,20,5,0) 75%, rgba(18,20,5,0.45) 100%),
      linear-gradient(160deg, rgba(154,26,20,0) 55%, rgba(154,26,20,0.75) 80%, rgba(60,10,8,0.9) 100%),
      linear-gradient(180deg, var(--chartreuse) 0%, #b9bd2c 25%, var(--olive) 50%, var(--moss) 72%, var(--night) 100%);
  }
  .presenter {
    position: absolute;
    left: 52px;
    top: 22px;
    margin: 0;
    color: var(--lemon);
    font-weight: 700;
    font-size: 34px;
    letter-spacing: 0.3px;
    text-transform: uppercase;
  }
  .show-title {
    position: absolute;
    inset: 0;
    margin: 0;
    font-family: "Lobster", cursive;
    font-weight: 400;
    line-height: 1;
    pointer-events: none;
  }
  .show-title span {
    position: absolute;
    display: block;
    white-space: nowrap;
    background: linear-gradient(180deg, var(--gold-top) 10%, var(--gold-bottom) 90%);
    -webkit-background-clip: text;
    background-clip: text;
    color: transparent;
    -webkit-text-stroke: 4px var(--outline-red);
    transform: rotate(-20deg);
    transform-origin: left bottom;
  }
  .title-a    { font-size: 380px; left: 40px;  top: 420px; }
  .title-plum { font-size: 220px; left: 190px; top: 370px; }
  .title-hush { font-size: 250px; left: 290px; top: 560px; }
  .show-date {
    position: absolute;
    left: 345px;
    top: 925px;
    margin: 0;
    font-family: "Roboto Condensed", sans-serif;
    font-weight: 700;
    font-size: 46px;
    color: var(--lemon);
    -webkit-text-stroke: 1.5px var(--outline-red);
    transform: rotate(-14deg);
    transform-origin: left bottom;
    white-space: nowrap;
  }
  .accent-star {
    position: absolute;
    left: 155px;
    top: 852px;
    width: 50px;
    height: 50px;
  }
  .sponsor-band {
    position: absolute;
    left: 0;
    bottom: 0;
    width: 100%;
    height: 102px;
    background: var(--band);
    display: flex;
    align-items: center;
    padding: 0 42px 0 46px;
    box-sizing: border-box;
  }
  .sponsor {
    font-family: "Oswald", sans-serif;
    font-weight: 600;
    font-size: 21px;
    color: var(--ink);
    display: flex;
    align-items: center;
    gap: 9px;
    margin-right: 34px;
    white-space: nowrap;
  }
  .sponsor-dot {
    width: 16px;
    height: 16px;
    border-radius: 50%;
    background: var(--ink);
  }
  .sponsor-square {
    width: 16px;
    height: 16px;
    background: var(--navy);
  }
  .contact {
    margin-left: auto;
    text-align: right;
    font-family: "Roboto Condensed", sans-serif;
    font-weight: 700;
    color: var(--ink);
    line-height: 1.1;
  }
  .contact-phone { font-size: 25px; }
  .contact-web { font-size: 38px; }
</style>
</head>
<body>
  <main class="poster">
    <div class="hero-photo" role="img" aria-label="Halftone photo of a lounge singer in a red halter dress holding a vintage microphone, in yellow-green tones"></div>

    <p class="presenter">VelNOVA Professional Series Presents</p>

    <h1 class="show-title" aria-label="A Plum Hush">
      <span class="title-a">A</span>
      <span class="title-plum">Plum</span>
      <span class="title-hush">Hush</span>
    </h1>

    <svg class="accent-star" viewBox="0 0 48 48" aria-hidden="true">
      <polygon points="24,2 30,18 47,18 33,28 38,46 24,35 10,46 15,28 1,18 18,18" fill="#e8a81f"/>
    </svg>

    <p class="show-date">DECEMBER 18th, 2015</p>

    <footer class="sponsor-band">
      <div class="sponsor"><span class="sponsor-dot"></span>Step Lively</div>
      <div class="sponsor"><span class="sponsor-square"></span>Orrin</div>
      <div class="sponsor"><span class="sponsor-dot"></span>Mira Lens Photography</div>
      <div class="contact">
        <div class="contact-phone">512-555-0148 EXT 207</div>
        <div class="contact-web">vel-nova.org</div>
      </div>
    </footer>
  </main>
</body>
</html>
```